Calloway Dental Care

I need a nice business card design that is double sided. This is for a dental surgery. I have already had a logo designed and just need the business card put together.

It needs to be in a format such that I can make new business cards if new dentists begin working for me. Hence I need to be able to change the text in order to have new names written on new cards.

The front will have the following text:

Dr Tariq Mansour
B. Med. Sci. QBTU B.Dent. Brel. Uni

The logo will appear somewhere on the front. This is attached.

In addition will be the following writing that also needs to appear on the front of the card, perhaps at the bottom on the left side will be:

Shop 4, 212-240 Parlow Street, North Sydney, NSW, 2060

and at the bottom on the right side will be:
(02) 5550 1736
e: info@callowaydentalcare.com.au
www.callowaydentalcare.com.au

On the back of the card will be a section for a map to be drawn (I have uploaded a picture) and also a section written as follows:

"Your next appointment is: (a line needs to be here to write date and time)"

Also I need two lines for two appointments to be written.

Thanks for your efforts!

```html
<!DOCTYPE html>
<html lang="en">
<head>
<meta charset="utf-8">
<title>Calloway Dental Care – Business Card</title>
<link href="https://fonts.googleapis.com/css2?family=Arimo:wght@400;700&display=swap" rel="stylesheet">
<style>
  :root {
    --bg: #231f20;
    --card: #ffffff;
    --brand-blue: #336699;
    --brand-cyan: #1ec0f0;
    --ink: #1a1a1a;
    --rule: #6b6b6b;
    --map-fill: #eef1f4;
  }
  * { margin: 0; padding: 0; box-sizing: border-box; }
  html, body { width: 1200px; height: 780px; overflow: hidden; }
  body { background: var(--bg); font-family: "Arimo", Arial, sans-serif; color: var(--ink); position: relative; }

  .card {
    position: absolute;
    width: 460px;
    height: 290px;
    background: var(--card);
    border-radius: 22px;
    overflow: hidden;
  }
  .card--front { left: 140px; top: 90px; }
  .card--back { left: 600px; top: 400px; }

  /* Front */
  .brand {
    position: absolute;
    top: 48px; left: 0; right: 0;
    display: flex; align-items: center; justify-content: center; gap: 12px;
  }
  .brand__dot { width: 28px; height: 28px; border-radius: 50%; background: var(--brand-blue); }
  .brand__name {
    font-size: 25px; font-weight: 400; color: var(--brand-blue);
    letter-spacing: 1px; text-transform: uppercase; white-space: nowrap;
  }
  .dentist { position: absolute; top: 140px; left: 0; right: 0; text-align: center; }
  .dentist__name { font-size: 17px; font-weight: 700; color: var(--brand-blue); letter-spacing: 0.5px; }
  .dentist__quals { font-size: 10px; font-weight: 700; margin-top: 3px; }
  .address, .contact { position: absolute; z-index: 1; font-size: 12px; line-height: 15px; white-space: nowrap; }
  .address { left: 38px; top: 200px; }
  .contact { left: 226px; top: 192px; }
  .contact span { display: inline-block; width: 28px; }
  .swoosh { position: absolute; left: 0; bottom: 0; width: 460px; height: 66px; }

  /* Back */
  .appointment { position: absolute; left: 26px; top: 46px; right: 26px; }
  .appointment__row { display: flex; align-items: flex-end; font-weight: 700; white-space: nowrap; }
  .appointment__lead { font-size: 14px; }
  .appointment__label { font-size: 10px; margin-left: 4px; }
  .blank { border-bottom: 1px solid var(--rule); height: 1px; }
  .blank--date { width: 62px; margin: 0 8px 3px 4px; }
  .blank--time { width: 62px; margin: 0 0 3px 4px; }
  .blank--line { width: 300px; margin-top: 20px; }
  .map {
    position: absolute; left: 176px; top: 130px; width: 150px; height: 140px;
    background: var(--map-fill); border-radius: 4px;
  }
  .brand--small {
    position: absolute; right: 20px; bottom: 26px;
    font-size: 9px; font-weight: 400; color: var(--brand-blue);
    text-transform: uppercase; letter-spacing: 0.3px; white-space: nowrap;
  }
</style>
</head>
<body>

  <section class="card card--front">
    <div class="brand">
      <span class="brand__dot"></span>
      <span class="brand__name">Calloway Dental Care</span>
    </div>
    <div class="dentist">
      <p class="dentist__name">Dr Tariq Mansour</p>
      <p class="dentist__quals">B Med Sci (QBTU), BDent (Brel. Uni)</p>
    </div>
    <p class="address">Shop 4, 212-240 Parlow<br>Street, North Sydney, 2060</p>
    <p class="contact"><span>Tel:</span>(02) 5550 1736<br><span>e:</span>info@callowaydentalcare.com.au</p>
    <svg class="swoosh" viewBox="0 0 460 66" preserveAspectRatio="none">
      <path d="M0 14 C130 34 310 34 460 6 L460 20 C320 46 150 48 0 36 Z" fill="var(--brand-cyan)"/>
      <path d="M0 42 C150 54 320 46 460 24 L460 66 L0 66 Z" fill="var(--brand-blue)"/>
    </svg>
  </section>

  <section class="card card--back">
    <div class="appointment">
      <div class="appointment__row">
        <span class="appointment__lead">Your next appointment is:</span>
        <span class="appointment__label">Date:</span><span class="blank blank--date"></span>
        <span class="appointment__label">Time:</span><span class="blank blank--time"></span>
      </div>
      <div class="blank blank--line"></div>
      <div class="blank blank--line"></div>
    </div>
    <div class="map" role="img" aria-label="Street map showing the location of Calloway Dental Care"></div>
    <p class="brand--small">Calloway Dental Care</p>
  </section>

</body>
</html>
```